CPA, Management and IT Consulting Redesign Existing Website

We currently have a website that is outdated (www.qelvarn.com). We need a good website developer that can redesign our website. To make this easier I have chosen a few websites that we like the layout or template. Use our exiting website content for this project. Our new logo is attached below. Based on who wins this we will upgrade to a coded website and a content management system (CMS) so we can make changes to the text ourselves in the future.

http://www.brontekhaile.com/
http://www.lorvicanmanagement.com/

Target Market(s)

Government Clients

Industry/Entity Type

Management Consulting

Number of Pages Required

5+ page

Font styles to use
Serif

Requirements
Must have
• Please the following website templates as a guide.
• http://www.brontekhaile.com/
• http://www.lorvicanmanagement.com/
Nice to have
Should not have

```html
<!DOCTYPE html>
<html lang="en">
<head>
<meta charset="utf-8">
<title>Corvell Enterprises, LLC</title>
<link rel="stylesheet" href="https://fonts.googleapis.com/css2?family=Roboto:wght@300;400;500;700&display=swap">
<style>
:root{
  --orange:#f7963f;
  --orange-soft:#fba867;
  --orange-line:#f3c79a;
  --dark:#252525;
  --ink:#222222;
  --body:#444444;
  --white:#ffffff;
  --green:#7cb83a;
}
*{margin:0;padding:0;box-sizing:border-box}
html,body{width:1200px;height:2413px;overflow:hidden;background:var(--white)}
body{position:relative;font-family:'Roboto',sans-serif;color:var(--ink)}
.abs{position:absolute}

/* header */
.brand{left:118px;top:16px;display:flex;align-items:center;gap:12px}
.brand-mark{width:46px;height:46px;background:var(--orange)}
.brand-name{font-size:34px;font-weight:700;color:var(--ink);line-height:1;letter-spacing:.5px}
.office{top:20px;font-size:11px;line-height:19px;color:var(--ink)}
.office h4{font-size:11px;font-weight:700;letter-spacing:.3px}
.office svg{vertical-align:-2px;margin-right:4px}
.office-divider{top:22px;width:1px;height:48px;background:#cfcfcf}
.social{left:1050px;width:17px;height:17px;border-radius:3px;background:#2f6db5}
.social.tw{background:#2aa3e0}

/* nav */
.nav-band{left:0;top:93px;width:1200px;height:76px;background:var(--orange)}
.nav{left:132px;top:108px;display:flex;font-size:15px;color:var(--white)}
.nav span{padding:0 18px;border-right:1px solid rgba(255,255,255,.45);line-height:24px}
.nav span:first-child{padding-left:18px}
.subnav{left:132px;top:146px;width:936px;height:47px;background:var(--dark);display:flex;align-items:center;padding-left:14px;gap:25px;font-size:14px;color:var(--white);z-index:3}

/* hero */
.hero{left:0;top:169px;width:1200px;height:343px;background:linear-gradient(135deg,#55575c 0%,#6d7179 45%,#4b4e55 100%)}
.hero-title{left:0;top:290px;width:1200px;text-align:center;font-size:66px;font-weight:400;color:var(--white)}

/* stats */
.stat{top:515px;width:300px;text-align:center;color:var(--orange)}
.stat b{display:block;font-size:92px;font-weight:300;line-height:100px}
.stat span{display:block;font-size:19px;margin-top:22px}

.rule{left:132px;width:936px;height:1px;background:var(--orange-line)}

/* section headings */
.heading{left:132px;display:flex;align-items:center;font-size:38px;color:var(--ink)}
.tag{background:var(--orange);color:var(--white);padding:0 6px;line-height:38px;margin-right:14px;letter-spacing:.5px}
.tag-small{left:132px;font-size:25px;background:var(--orange);color:var(--white);padding:0 6px;line-height:28px;letter-spacing:.5px}

.copy{left:132px;width:458px;font-size:13.5px;line-height:20px;color:var(--body)}
.copy p+p{margin-top:20px}

.photo{background:linear-gradient(160deg,#3b4d8a 0%,#9a6c5a 45%,#c89a6a 70%,#b89a86 100%)}
.caption{left:618px;top:1103px;font-size:11px;color:var(--white)}
.portrait{top:1261px;width:210px;height:209px;background:linear-gradient(180deg,#8e8a83 0%,#6f6a64 100%)}
.name{top:1488px;font-size:17px;font-weight:700;color:var(--ink)}
.role{top:1524px;font-size:11px;color:var(--body)}

/* client cards */
.card{top:1684px;width:300px;height:243px;padding:18px 18px;color:var(--white)}
.card.light{background:var(--orange-soft)}
.card.mid{background:var(--orange)}
.card h3{font-size:26px;font-weight:400;line-height:28px}
.card p{margin-top:14px;font-size:13.5px;line-height:20px;font-weight:500}

/* footer */
.foot-dark{left:0;top:2003px;width:431px;height:410px;background:var(--dark)}
.foot-orange{left:431px;top:2043px;width:769px;height:370px;background:var(--orange)}
.foot-brand{left:161px;top:2040px;display:flex;align-items:center;gap:10px}
.foot-brand .brand-mark{width:40px;height:40px}
.foot-brand .brand-name{font-size:30px;color:var(--white)}
.foot-contact{left:173px;font-size:13px;font-weight:500;color:var(--white)}
.foot-contact svg{vertical-align:-2px;margin-right:5px}
.foot-col{top:2074px;width:150px;color:var(--white)}
.foot-col h5{font-size:16px;font-weight:400;line-height:28px;margin-bottom:14px}
.foot-col li{list-style:none;font-size:12px;line-height:19px;margin-bottom:15px;padding-left:14px;position:relative;color:#fff4e8}
.foot-col li::before{content:"›";position:absolute;left:0;top:0}
.foot-col li.active{font-weight:500;color:var(--white)}
</style>
</head>
<body>

<!-- header -->
<div class="abs brand"><div class="brand-mark"></div><div class="brand-name">CORVELL</div></div>

<div class="abs office" style="left:450px">
  <h4>OFFICE WASHINGTON</h4>
  <div><svg width="10" height="10" viewBox="0 0 10 10"><path d="M5 1 1 5h1.5v4h5V5H9z" fill="#7cb83a"/></svg>418 Lanterne Street NW, Suite 300</div>
  <div><svg width="10" height="10" viewBox="0 0 10 10"><path d="M2 1h2l1 2.5-1.3 1a6 6 0 0 0 2.8 2.8l1-1.3L10 7v2c-5 0-8-3-8-8z" fill="#7cb83a"/></svg>(202) 555-0148</div>
</div>
<div class="abs office-divider" style="left:608px"></div>
<div class="abs office" style="left:623px">
  <h4>OFFICE GREENBELT</h4>
  <div><svg width="10" height="10" viewBox="0 0 10 10"><path d="M5 1 1 5h1.5v4h5V5H9z" fill="#7cb83a"/></svg>5270 Harrow Road, Suite 407</div>
  <div><svg width="10" height="10" viewBox="0 0 10 10"><path d="M2 1h2l1 2.5-1.3 1a6 6 0 0 0 2.8 2.8l1-1.3L10 7v2c-5 0-8-3-8-8z" fill="#7cb83a"/></svg>(301) 555-0172</div>
</div>
<div class="abs office-divider" style="left:806px"></div>
<div class="abs office" style="left:821px">
  <h4>OFFICE NEWARK</h4>
  <div><svg width="10" height="10" viewBox="0 0 10 10"><path d="M5 1 1 5h1.5v4h5V5H9z" fill="#7cb83a"/></svg>72 Meridian Avenue, Suite 201 C</div>
  <div><svg width="10" height="10" viewBox="0 0 10 10"><path d="M2 1h2l1 2.5-1.3 1a6 6 0 0 0 2.8 2.8l1-1.3L10 7v2c-5 0-8-3-8-8z" fill="#7cb83a"/></svg>(301) 555-0172</div>
</div>
<div class="abs office-divider" style="left:1006px"></div>
<div class="abs social" style="top:22px"></div>
<div class="abs social tw" style="top:52px"></div>

<!-- navigation -->
<div class="abs nav-band"></div>
<nav class="abs nav">
  <span>HOME</span><span>ABOUT US</span><span>SERVICES</span><span>INDUSTRIES</span><span>BLOG</span><span>CONTACT US</span>
</nav>
<div class="abs subnav">
  <span>Federal Government</span><span>State and Local Government</span><span>Financial Services</span><span>Not-For-Profit</span>
</div>

<!-- hero -->
<div class="abs hero" role="img" aria-label="Desaturated photo of hands reviewing printed financial charts"></div>
<h1 class="abs hero-title">Complex challenges</h1>

<!-- stats -->
<div class="abs stat" style="left:131px"><b>623</b><span>Satisfied Clients</span></div>
<div class="abs stat" style="left:449px"><b>250</b><span>Finishes Projects</span></div>
<div class="abs stat" style="left:767px"><b>351</b><span>Days of Work</span></div>

<div class="abs rule" style="top:722px"></div>

<!-- welcome -->
<h2 class="abs heading" style="top:774px"><span class="tag">WELCOME</span>| Corvell Enterprises, LLC</h2>
<div class="abs copy" style="top:867px">
  <p>Corvell Enterprises, LLC and Ashby &amp; Morrow, LLC is a network of certified public accounting and management consulting firms with seasoned professionals and an excellent reputation for serving a diverse client base including federal agencies, state and local government, non-profit organizations, small and medium-sized business entities, professional associations and individuals.</p>
  <p>We are committed to professional excellence across all service areas including Audit and Assurance, Accounting, Tax, Management Consulting, and Information Technology. Find out more.</p>
</div>
<div class="abs photo" style="left:610px;top:867px;width:458px;height:261px" role="img" aria-label="Photo of a national flag, a historic document and a capitol dome"></div>
<div class="abs caption">We provide a variety of services to government entities</div>

<div class="abs rule" style="top:1213px"></div>

<!-- management -->
<h2 class="abs tag-small" style="top:1260px">MANAGEMENT</h2>
<div class="abs copy" style="top:1304px">
  <p>Our management team consists of a unique blend of highly skilled professionals who bring significant experience in assurance and advisory services in both the public and private sectors</p>
  <p>Our management team is a highly energetic and client facing and are licensed Certified Public Accountants (CPAs), Masters of Business Administration (MBAs), Certified Fraud Examiners (CFE), Project Management Professionals (PMP), Certified Information System Auditors (CISA), and Certified Government Financial Managers (CGFM).</p>
</div>
<div class="abs portrait" style="left:610px" role="img" aria-label="Portrait photo of principal Renata Corvell"></div>
<div class="abs portrait" style="left:840px" role="img" aria-label="Portrait photo of principal Dorian Corvell"></div>
<div class="abs name" style="left:610px">Renata Corvell</div>
<div class="abs name" style="left:840px">Dorian Corvell</div>
<div class="abs role" style="left:610px">Principal</div>
<div class="abs role" style="left:840px">Principal</div>

<div class="abs rule" style="top:1581px"></div>

<!-- clients -->
<h2 class="abs heading" style="top:1630px"><span class="tag">CLIENTS</span>| We offer our clients a full scope of business</h2>
<div class="abs card light" style="left:132px">
  <h3>Federal<br>Clients</h3>
  <p>Lorem ipsum dolor sit amet, consetetur sadipscing elitr, sed diam nonumy eirmod tempor invidunt ut labore et dolore magna aliquyam erat, sed diam voluptua. At vero eos et accusam et justo duo dolores et ea rebum. Stet clita kasd gubergren,</p>
</div>
<div class="abs card mid" style="left:450px">
  <h3>State and Local<br>Government Clients</h3>
  <p>Lorem ipsum dolor sit amet, consetetur sadipscing elitr, sed diam nonumy eirmod tempor invidunt ut labore et dolore magna aliquyam erat, sed diam voluptua. At vero eos et accusam et justo duo dolores et ea rebum. Stet clita kasd gubergren,</p>
</div>
<div class="abs card mid" style="left:769px">
  <h3>Commercial<br>Clients</h3>
  <p>Lorem ipsum dolor sit amet, consetetur sadipscing elitr, sed diam nonumy eirmod tempor invidunt ut labore et dolore magna aliquyam erat, sed diam voluptua. At vero eos et accusam et justo duo dolores et ea rebum. Stet clita kasd gubergren,</p>
</div>

<!-- footer -->
<div class="abs foot-dark"></div>
<div class="abs foot-orange"></div>
<div class="abs foot-brand"><div class="brand-mark"></div><div class="brand-name">CORVELL</div></div>
<div class="abs foot-contact" style="top:2130px"><svg width="11" height="11" viewBox="0 0 10 10"><path d="M5 1 1 5h1.5v4h5V5H9z" fill="#7cb83a"/></svg>418 Lanterne Street NW, Suite 300</div>
<div class="abs foot-contact" style="top:2169px"><svg width="11" height="11" viewBox="0 0 10 10"><path d="M5 1 1 5h1.5v4h5V5H9z" fill="#7cb83a"/></svg>Washington, DC 20099</div>
<div class="abs foot-contact" style="top:2207px"><svg width="11" height="11" viewBox="0 0 10 10"><path d="M2 1h2l1 2.5-1.3 1a6 6 0 0 0 2.8 2.8l1-1.3L10 7v2c-5 0-8-3-8-8z" fill="#7cb83a"/></svg>(202) 555-0148</div>
<div class="abs foot-contact" style="top:2246px"><svg width="11" height="11" viewBox="0 0 10 10"><rect x="2.5" y="1" width="5" height="8" rx="1" fill="none" stroke="#7cb83a" stroke-width="1.2"/></svg>(202) 555-0193</div>

<div class="abs foot-col" style="left:444px">
  <h5>Services and<br>Solutions</h5>
  <ul><li>Audit, Accounting and Tax</li><li>Financial Management</li><li>Information Technology</li><li>Governance, Risk and Compliance</li></ul>
</div>
<div class="abs foot-col" style="left:600px">
  <h5>Industries</h5>
  <ul><li>Federal Government</li><li>State and Local Government</li><li>Financial Services</li><li>Not-for-Profit</li></ul>
</div>
<div class="abs foot-col" style="left:759px">
  <h5>Industries</h5>
  <ul><li class="active">Federal Government</li><li>State and Local Government</li><li>Financial Services</li><li>Not-For-Profit</li></ul>
</div>
<div class="abs foot-col" style="left:917px">
  <h5>About Us</h5>
  <ul><li>Company Overview</li><li>Management</li><li>Clients</li><li>Careers</li></ul>
</div>

</body>
</html>
```